Logo and Business Card Design for Innovative Corporate Law Firm

Valmor Advogados is a new, young and innovative law firm focused in corporate law, mainly helping start-ups in the incorporation process, liasing with strategic investors, funds, private equity and venture/seed capital businesses around the world.

We need a logo and business card design that correctly captures our modern and savvy, yet sober, approach to legal practice.

We are looking to starting with the logo and business card designs and further ahead move on to stationery, website etc.

We are located in São Paulo/Brazil, but we expect our logo and stationery design to be able to reach and connect to possible clients worldwide due to the international characteristic of our practice.

Be creative! We have no restrictions on colors, one-sided or two-sided cards, logos, font styles...
Updates

Guys, just to be clear: The project shall contemplate a full stationery design, but the logo and business card may be proposed in advance due to our urgent need to have these cards ready for our clients. The other stationery items may be proposed later on. Many thanks!

Dear all, please be aware that the logo should look good both in collor and black and white. 

Thanks

Industry/Entity Type

Business

Requirements
Must have
• Modern but sober approach
Nice to have
• I tend to like grey collor schemes with red touches, but this is not a must have...
Should not have
• Excessively bright, shiny look, that will make our legal services look too commercial. No excesses.

```html
<!DOCTYPE html>
<html lang="en">
<head>
<meta charset="utf-8">
<title>Valmor Advogados — business card concepts</title>
<link rel="stylesheet" href="https://fonts.googleapis.com/css2?family=Marcellus&family=Crimson+Text&family=Archivo+Narrow:wght@700&display=swap">
<style>
  :root {
    --brand-green: #76bf44;
    --paper: #ffffff;
    --ink: #111111;
  }
  html, body {
    margin: 0;
    padding: 0;
    overflow: hidden;
    background: var(--paper);
  }
  .canvas {
    position: relative;
    width: 948px;
    height: 1200px;
    overflow: hidden;
    background: var(--paper);
    font-family: "Marcellus", serif;
  }
  .card {
    position: absolute;
    box-sizing: border-box;
    overflow: hidden;
  }
  .card--green { background: var(--brand-green); color: var(--paper); }
  .card--white { background: var(--paper); border: 2px solid var(--ink); color: var(--brand-green); }

  .wordmark {
    position: absolute;
    margin: 0;
    font-family: "Marcellus", serif;
    font-weight: 400;
    line-height: 0.95;
    white-space: nowrap;
  }
  .tagline {
    position: absolute;
    margin: 0;
    font-family: "Marcellus", serif;
    letter-spacing: 0.22em;
    white-space: nowrap;
  }
  .tagline--vertical { writing-mode: vertical-rl; }

  .contact {
    position: absolute;
    margin: 0;
    text-align: right;
    font-family: "Marcellus", serif;
    white-space: nowrap;
  }
  .contact p { margin: 0; }

  /* concept 1: rounded card */
  .card--rounded {
    left: 31px; top: 4px; width: 434px; height: 247px;
    border: 1.5px solid var(--ink); border-radius: 41px; background: var(--paper);
  }
  .logo-tile {
    position: absolute; left: -1px; top: -1px; width: 171px; height: 171px;
    background: var(--brand-green); border-radius: 26px;
  }
  .card--rounded .wordmark { left: 12px; top: 50px; font-size: 29px; color: var(--paper); }
  .card--rounded .tagline { left: 176px; top: 22px; font-size: 13px; color: var(--brand-green); }
  .card--rounded .contact {
    right: 13px; top: 176px; font-family: "Crimson Text", serif;
    font-size: 12px; line-height: 16.5px; color: var(--brand-green);
  }

  /* concept 2: green front + back */
  .front-a { left: 0; top: 288px; width: 434px; height: 248px; }
  .front-a .wordmark { left: 70px; top: 30px; font-size: 64px; }
  .front-a .tagline { left: 66px; top: 196px; font-size: 31px; }
  .side-label {
    position: absolute; left: 444px; top: 350px; margin: 0;
    font-family: "Archivo Narrow", sans-serif; font-weight: 700; font-size: 19px;
    color: var(--ink); letter-spacing: -0.02em;
  }
  .back-a { left: 2px; top: 546px; width: 434px; height: 248px; }
  .back-a .contact { right: 10px; top: 170px; font-size: 18px; line-height: 25px; }

  /* concept 3: white card */
  .card-white { left: 4px; top: 806px; width: 434px; height: 248px; }
  .card-white .wordmark { left: 20px; top: 20px; font-size: 48px; color: var(--brand-green); }
  .card-white .tagline { left: 18px; top: 136px; font-size: 23px; }
  .card-white .contact { right: 10px; top: 176px; font-size: 16.5px; line-height: 20.5px; }

  /* concept 4: vertical tagline */
  .front-b { left: 514px; top: 529px; width: 434px; height: 248px; }
  .front-b .wordmark { left: 22px; top: 66px; font-size: 52px; }
  .front-b .tagline { left: 322px; top: 18px; font-size: 22px; }
  .back-b { left: 504px; top: 801px; width: 435px; height: 248px; }
  .back-b .contact { right: 13px; top: 168px; font-size: 18px; line-height: 25px; }

  .stray-mark {
    position: absolute; left: 96px; top: 1156px; width: 5px; height: 2px;
    background: var(--brand-green);
  }
</style>
</head>
<body>
<main class="canvas">

  <section class="card card--rounded" aria-label="Rounded business card">
    <div class="logo-tile"></div>
    <h2 class="wordmark">Valmor<br>Advogados</h2>
    <p class="tagline tagline--vertical">corporate law</p>
    <div class="contact">
      <p>Brisa Communications</p>
      <p>415•555•010</p>
      <p>www.brisacommunications.com</p>
    </div>
  </section>

  <section class="card card--green front-a" aria-label="Card front">
    <h2 class="wordmark">Valmor<br>Advogados</h2>
    <p class="tagline">corporate law</p>
  </section>
  <p class="side-label">front</p>

  <section class="card card--green back-a" aria-label="Card back">
    <div class="contact">
      <p>Brisa Communications</p>
      <p>415•555•010</p>
      <p>www.brisacommunications.com</p>
    </div>
  </section>

  <section class="card card--white card-white" aria-label="White business card">
    <h2 class="wordmark">Valmor<br>Advogados</h2>
    <p class="tagline">corporate law</p>
    <div class="contact">
      <p>Brisa Communications</p>
      <p>415•555•010</p>
      <p>www.brisacommunications.com</p>
    </div>
  </section>

  <section class="card card--green front-b" aria-label="Card front with vertical tagline">
    <h2 class="wordmark">Valmor<br>Advogados</h2>
    <p class="tagline tagline--vertical">corporate law</p>
  </section>

  <section class="card card--green back-b" aria-label="Card back">
    <div class="contact">
      <p>Brisa Communications</p>
      <p>415•555•010</p>
      <p>www.brisacommunications.com</p>
    </div>
  </section>

  <div class="stray-mark"></div>
</main>
</body>
</html>
```